New Business Cards for MB&LR

We need updated business cards for a staff of 15 engineers, estimators, project managers, and sales people. We have recently begun changes to our website and marketing material to improve our look and branding. We are an established fabricator specializing in pressure vessels, tanks, and structural steel. The owners require us to use the existing logo and old english text design. Also, we prefer dark grey or mostly black cards.
Target Market(s)
Engineers, purchasing agents, estimators, and project managers of; mining companies, refineries, industrial construction professionals
Industry/Entity Type
Business
Contact Information for Business Card
Logo, phone, website, email, etc.
Look and feel

```html
<!DOCTYPE html>
<html lang="en">
<head>
<meta charset="utf-8">
<title>MB&amp;LR Business Cards</title>
<link rel="stylesheet" href="https://fonts.googleapis.com/css2?family=Michroma&family=Josefin+Sans:wght@300;400;600&display=swap">
<style>
  :root {
    --backdrop: #2e2e2e;
    --steel-dark: #8e8e8e;
    --steel-mid: #c4c4c4;
    --steel-light: #ececec;
    --panel-black: #050505;
    --mark-grey: #8a8a8a;
    --ink: #111111;
    --icon-white: #ffffff;
  }
  * { margin: 0; padding: 0; box-sizing: border-box; }
  html, body { width: 1200px; height: 776px; overflow: hidden; }
  body {
    background: var(--backdrop);
    position: relative;
    font-family: "Josefin Sans", sans-serif;
  }
  .card {
    position: absolute;
    width: 600px;
    height: 350px;
    overflow: hidden;
    background:
      repeating-linear-gradient(0deg, rgba(255,255,255,0.06) 0 1px, rgba(0,0,0,0.04) 1px 2px),
      linear-gradient(100deg, var(--steel-dark) 0%, var(--steel-light) 30%, var(--steel-mid) 55%, var(--steel-light) 78%, var(--steel-dark) 100%);
    box-shadow: 0 6px 18px rgba(0,0,0,0.5);
  }
  .card--front { left: 50px; top: 40px; }
  .card--back { left: 550px; top: 390px; }
  .card__panel { position: absolute; inset: 0; }

  .front__tagline {
    position: absolute;
    right: 40px;
    top: 28px;
    font-family: "Michroma", sans-serif;
    font-size: 17px;
    line-height: 1.35;
    color: var(--mark-grey);
    text-align: right;
    letter-spacing: 0.5px;
  }
  .brand-mark {
    position: absolute;
    display: flex;
    align-items: center;
    gap: 8px;
    color: var(--mark-grey);
    font-family: "Josefin Sans", sans-serif;
    font-weight: 600;
  }
  .brand-mark__dot {
    border-radius: 50%;
    border: 3px solid var(--mark-grey);
  }
  .front__brand { left: 448px; top: 135px; font-size: 22px; }
  .front__brand .brand-mark__dot { width: 18px; height: 18px; }

  .front__badge {
    position: absolute;
    left: 500px;
    top: 240px;
    width: 72px;
    height: 72px;
    border-radius: 50%;
    background: #1b1b1b;
  }

  .holder { position: absolute; left: 55px; top: 160px; color: var(--ink); }
  .holder__name { font-size: 21px; font-weight: 400; letter-spacing: 0.5px; }
  .holder__position { font-size: 19px; font-weight: 300; margin-left: 85px; margin-top: 4px; color: #222; }

  .contact { position: absolute; left: 55px; top: 222px; list-style: none; color: var(--ink); }
  .contact__item { display: flex; align-items: flex-start; gap: 12px; font-size: 20px; margin-bottom: 9px; letter-spacing: 0.5px; }
  .contact__icon { width: 26px; height: 26px; flex: none; margin-top: -3px; }
  .contact__address { line-height: 1.15; }

  .back__brand { left: 210px; top: 110px; font-size: 48px; }
  .back__brand .brand-mark__dot { width: 34px; height: 34px; border-width: 5px; }
  .back__web {
    position: absolute;
    left: 250px;
    top: 265px;
    font-size: 18px;
    color: var(--mark-grey);
    letter-spacing: 0.5px;
  }
</style>
</head>
<body>

<section class="card card--front" aria-label="Business card front">
  <svg class="card__panel" viewBox="0 0 600 350" width="600" height="350">
    <path fill="var(--panel-black)" d="M0,0 H600 V140 Q600,150 592,158 L562,192 Q552,204 532,205 Q480,207 445,194 L0,28 Z"/>
  </svg>
  <p class="front__tagline">MESA BEAM &amp; LINER<br>ROLLING</p>
  <div class="brand-mark front__brand"><span class="brand-mark__dot"></span>MB&amp;LR</div>
  <div class="front__badge" aria-label="Anniversary badge"></div>

  <div class="holder">
    <p class="holder__name">HOLDER’S NAME</p>
    <p class="holder__position">Position</p>
  </div>

  <ul class="contact">
    <li class="contact__item">
      <svg class="contact__icon" viewBox="0 0 26 26"><circle cx="13" cy="13" r="13" fill="var(--ink)"/><path fill="var(--icon-white)" d="M9 6.5l2.3 2.6-1.3 2a9 9 0 0 0 4.9 4.9l2-1.3 2.6 2.3-1.4 2.3C12.5 19 7 13.5 6.8 7.9z"/></svg>
      <span>555-014-2290</span>
    </li>
    <li class="contact__item">
      <svg class="contact__icon" viewBox="0 0 26 26"><circle cx="13" cy="13" r="13" fill="var(--ink)"/><rect x="7" y="8.5" width="12" height="9" fill="none" stroke="var(--icon-white)" stroke-width="1.4"/><path d="M7 8.5l6 5 6-5M7 17.5l4.5-4.5M19 17.5l-4.5-4.5" fill="none" stroke="var(--icon-white)" stroke-width="1.2"/></svg>
      <span>jordan@mbandlr.com</span>
    </li>
    <li class="contact__item">
      <svg class="contact__icon" viewBox="0 0 26 26"><circle cx="13" cy="13" r="13" fill="var(--ink)"/><path fill="none" stroke="var(--icon-white)" stroke-width="1.6" d="M13 20s-5-5.2-5-9a5 5 0 0 1 10 0c0 3.8-5 9-5 9z"/><circle cx="13" cy="11" r="1.8" fill="var(--icon-white)"/></svg>
      <span class="contact__address">48 Foundry Row<br>Millbrook, UT 84000</span>
    </li>
  </ul>
</section>

<section class="card card--back" aria-label="Business card back">
  <svg class="card__panel" viewBox="0 0 600 350" width="600" height="350">
    <path fill="var(--panel-black)" d="M185,0 H545 L512,298 Q508,330 476,327 L165,288 Q128,283 131,252 L145,120 Z"/>
  </svg>
  <div class="brand-mark back__brand"><span class="brand-mark__dot"></span>MB&amp;LR</div>
  <p class="back__web">www.mbandlr.com</p>
</section>

</body>
</html>
```